new roofing company card

New primary business card for roofing company.

Industry/Entity Type

Residential roofing/Specializing in Asphalt and Standing seam metal roofing

Contact Information for Business Card

Phone number is: 484 672 1058 Email: support@fennridgeroofworks.com website: www.fennridgeroofworks.com

Colors
EB3D1F
EC4F4E
F09395
F8D3D4
FCEDEE

```html
<!DOCTYPE html>
<html lang="en">
<head>
<meta charset="utf-8">
<title>Fennridge Roofworks – Business Card</title>
<link href="https://fonts.googleapis.com/css2?family=Cinzel:wght@400;600&family=Roboto:wght@400&display=swap" rel="stylesheet">
<style>
  :root {
    --bg: #2d2d2d;
    --card: #000000;
    --red: #c8302a;
    --white: #ffffff;
  }
  * { margin: 0; padding: 0; box-sizing: border-box; }
  html, body {
    width: 1200px; height: 1015px; overflow: hidden;
    background: var(--bg);
  }
  .canvas {
    position: relative; width: 1200px; height: 1015px;
  }
  .card {
    position: absolute; left: 250px; width: 700px; height: 400px;
    background: var(--card);
    box-shadow: 0 10px 30px rgba(0,0,0,.6);
    overflow: hidden;
  }
  .card--front { top: 70px; }
  .card--back { top: 545px; }
  .card svg.frame { position: absolute; inset: 0; }

  .brand {
    position: absolute; left: 0; right: 0; top: 195px;
    text-align: center;
    font-family: "Cinzel", serif; font-weight: 600;
    color: var(--white);
    line-height: 1;
  }
  .brand__name { display: block; font-size: 58px; letter-spacing: 2px; }
  .brand__sub { display: block; font-size: 24px; letter-spacing: 8px; margin-top: 12px; }

  .holder {
    position: absolute; left: 90px; top: 225px;
  }
  .holder__name {
    font-family: "Cinzel", serif; font-weight: 400;
    font-size: 24px; color: var(--white); letter-spacing: 1px;
  }
  .holder__title {
    font-family: "Roboto", sans-serif; font-size: 17px;
    color: var(--red); margin-top: 2px;
  }
  .mark {
    position: absolute; right: 50px; top: 120px; width: 230px;
    text-align: center;
    font-family: "Cinzel", serif; font-weight: 600;
    color: var(--white); font-size: 34px; line-height: 1.15;
  }
  .contacts {
    position: absolute; left: 170px; top: 300px;
    list-style: none;
    font-family: "Roboto", sans-serif; font-size: 16px; color: var(--white);
  }
  .contacts li { display: flex; align-items: center; gap: 10px; height: 24px; }
  .contacts svg { width: 16px; height: 16px; flex: none; }
</style>
</head>
<body>
<main class="canvas">

  <section class="card card--front" aria-label="Card front">
    <svg class="frame" viewBox="0 0 700 400" aria-hidden="true">
      <polygon points="40,250 280,55 690,20 690,28 290,71 40,256" fill="var(--red)"/>
      <rect x="70" y="374" width="630" height="7" fill="var(--red)"/>
    </svg>
    <h1 class="brand">
      <span class="brand__name">FENNRIDGE</span>
      <span class="brand__sub">ROOFWORKS</span>
    </h1>
  </section>

  <section class="card card--back" aria-label="Card back">
    <svg class="frame" viewBox="0 0 700 400" aria-hidden="true">
      <polygon points="50,230 325,98 690,38 690,46 335,116 50,236" fill="var(--red)"/>
      <rect x="70" y="374" width="630" height="7" fill="var(--red)"/>
    </svg>
    <div class="mark">FENNRIDGE<br>ROOFWORKS</div>
    <div class="holder">
      <p class="holder__name">DANIEL WHITMORE</p>
      <p class="holder__title">Managing Director</p>
    </div>
    <ul class="contacts">
      <li>
        <svg viewBox="0 0 16 16" aria-hidden="true"><path d="M3 1.5l3 2.5-1.3 2.2a9 9 0 0 0 5.1 5.1L12 10l2.5 3-1.8 1.8C7 14.5 1.5 9 1.2 3.3z" fill="var(--red)"/></svg>
        <span>484 672 1058</span>
      </li>
      <li>
        <svg viewBox="0 0 16 16" aria-hidden="true"><rect x="1" y="3" width="14" height="10" fill="var(--red)"/><path d="M1 3l7 6 7-6" fill="none" stroke="#000" stroke-width="1.3"/></svg>
        <span>support@fennridgeroofworks.com</span>
      </li>
      <li>
        <svg viewBox="0 0 16 16" aria-hidden="true"><g fill="none" stroke="var(--red)" stroke-width="1.4"><circle cx="8" cy="8" r="6.5"/><ellipse cx="8" cy="8" rx="3" ry="6.5"/><path d="M1.5 8h13M2.5 4.8h11M2.5 11.2h11"/></g></svg>
        <span>www.fennridgeroofworks.com</span>
      </li>
    </ul>
  </section>

</main>
</body>
</html>
```